We need a business card design for a Dubai based company .

We need a business card for a Dubai based company called "Zernova Smoking Requisites Trading LLC". We mainly import Flavoured Tobacco products and Charcoal which is used for smoking in a Hookah/Shisha and distribute to the wholesalers and retailers. Logo file is attached herewith.

```html
<!DOCTYPE html>
<html lang="en">
<head>
<meta charset="utf-8">
<title>Zernova Smoking Requisites Trading LLC – Business Card</title>
<link rel="stylesheet" href="https://fonts.googleapis.com/css2?family=Roboto:wght@400;500;700&display=swap">
<style>
  :root {
    --backdrop: #d9d9d9;
    --card: #ffffff;
    --ink: #1e1e1e;
    --accent: #c6323a;
    --shadow: rgba(0, 0, 0, 0.18);
  }
  * { box-sizing: border-box; margin: 0; padding: 0; }
  html, body {
    width: 1200px; height: 900px; overflow: hidden;
    background: var(--backdrop);
    font-family: "Roboto", Arial, sans-serif;
    color: var(--ink);
  }
  .sheet {
    position: relative; width: 1200px; height: 900px;
    display: flex; flex-direction: column; align-items: center; justify-content: center; gap: 40px;
  }
  .card {
    position: relative; width: 700px; height: 400px;
    background: var(--card);
    box-shadow: 0 6px 18px var(--shadow);
    overflow: hidden;
  }
  /* Front */
  .edge-bar { position: absolute; background: var(--accent); }
  .edge-bar--top    { top: 0; left: 64%; width: 11px; height: 44px; }
  .edge-bar--bottom { bottom: 0; left: 34%; width: 11px; height: 44px; }
  .edge-bar--left   { left: 0; top: 36%; width: 44px; height: 11px; }
  .edge-bar--right  { right: 0; top: 62%; width: 44px; height: 11px; }
  .brand {
    display: flex; align-items: center; gap: 14px;
  }
  .brand__square {
    width: 18px; height: 18px; background: var(--accent); flex: none;
  }
  .brand__name {
    font-weight: 500; color: var(--ink); letter-spacing: 0.06em; line-height: 1.25;
  }
  .card--front .brand {
    position: absolute; inset: 0; justify-content: center;
  }
  .card--front .brand__name { font-size: 28px; max-width: 360px; }
  /* Back */
  .card--back .brand {
    position: absolute; top: 96px; right: 48px;
  }
  .card--back .brand__name { font-size: 18px; max-width: 230px; }
  .person { position: absolute; left: 60px; top: 150px; }
  .person__name { font-size: 30px; font-weight: 700; letter-spacing: -0.01em; }
  .person__role { font-size: 22px; font-weight: 500; color: var(--accent); margin-top: 2px; }
  .contact { position: absolute; left: 60px; top: 262px; list-style: none; }
  .contact__item {
    display: flex; align-items: center; gap: 12px;
    font-size: 17px; font-weight: 400; margin-bottom: 11px;
  }
  .contact__icon { width: 17px; height: 17px; flex: none; }
</style>
</head>
<body>
<main class="sheet">
  <section class="card card--front" aria-label="Card front">
    <span class="edge-bar edge-bar--top"></span>
    <span class="edge-bar edge-bar--right"></span>
    <span class="edge-bar edge-bar--bottom"></span>
    <span class="edge-bar edge-bar--left"></span>
    <div class="brand">
      <span class="brand__square"></span>
      <span class="brand__name">Zernova Smoking Requisites Trading LLC</span>
    </div>
  </section>

  <section class="card card--back" aria-label="Card back">
    <div class="person">
      <h1 class="person__name">Marek Dolinski</h1>
      <p class="person__role">Partner</p>
    </div>
    <ul class="contact">
      <li class="contact__item">
        <svg class="contact__icon" viewBox="0 0 24 24" aria-hidden="true"><path fill="#1e1e1e" d="M6.6 10.8a15 15 0 0 0 6.6 6.6l2.2-2.2c.3-.3.7-.4 1-.2 1.1.4 2.3.6 3.6.6.6 0 1 .4 1 1V20c0 .6-.4 1-1 1A17 17 0 0 1 3 4c0-.6.4-1 1-1h3.5c.6 0 1 .4 1 1 0 1.3.2 2.5.6 3.6.1.3 0 .7-.2 1z"/></svg>
        <span>555-010-2846</span>
      </li>
      <li class="contact__item">
        <svg class="contact__icon" viewBox="0 0 24 24" aria-hidden="true"><path fill="#1e1e1e" d="M2 5h20v14H2z"/><path fill="none" stroke="#fff" stroke-width="1.8" d="M2.5 6l9.5 7 9.5-7"/></svg>
        <span>hello@zernova-trade.com</span>
      </li>
      <li class="contact__item">
        <svg class="contact__icon" viewBox="0 0 24 24" aria-hidden="true"><g fill="none" stroke="#1e1e1e" stroke-width="1.8"><circle cx="12" cy="12" r="9.5"/><ellipse cx="12" cy="12" rx="4.2" ry="9.5"/><path d="M2.5 12h19M4 7h16M4 17h16"/></g></svg>
        <span>zernova-trade.com</span>
      </li>
    </ul>
    <div class="brand">
      <span class="brand__square"></span>
      <span class="brand__name">Zernova Smoking Requisites Trading LLC</span>
    </div>
  </section>
</main>
</body>
</html>
```